DRIFTFRAME studio

Design to be modern with colours of logo, maybe orange background. Include name, position, phone/WhatsApp email/web. Specialises in long form TIMELAPSE

Contact Information for Business Card

Marcus Ellery, filmmaker,/photographer, phone/WhatsApp +971528306457, email - marcus@driftframestudio.example www.driftframestudio.example, instagram @driftframestudio

Font styles to use
Sans Serif

Requirements
Must have
• Fresh, bright, modern, original
Marcus Ellery - Filmmaker/Photographer
Phone/WhatsApp +971 528 30 6457
email - marcus@driftfarmestudio.example
Web - driftfarmestudio.example
PoBox 584193, Dubai, UAE
instagram - driftframestudio
Should not have
• solid black background

```html
<!DOCTYPE html>
<html lang="en">
<head>
<meta charset="utf-8">
<title>DRIFTFRAME studio – Business Card</title>
<link rel="stylesheet" href="https://fonts.googleapis.com/css2?family=Montserrat:wght@400;500;800&display=swap">
<style>
  :root {
    --backdrop: #3b3b3d;
    --charcoal-top: #34343a;
    --charcoal-bottom: #26262b;
    --orange: #f47a1f;
    --orange-light: #ff9a3c;
    --orange-deep: #e0620c;
    --white: #ffffff;
    --soft: #e6e6e6;
  }
  * { margin: 0; padding: 0; box-sizing: border-box; }
  html, body { width: 1200px; height: 1015px; overflow: hidden; }
  body {
    background: var(--backdrop);
    font-family: "Montserrat", Arial, sans-serif;
    display: flex;
    flex-direction: column;
    align-items: center;
    justify-content: center;
    gap: 60px;
  }
  .card {
    position: relative;
    width: 700px;
    height: 400px;
    box-shadow:
      0 4px 0 var(--orange),
      0 8px 0 var(--charcoal-bottom),
      0 12px 0 var(--orange),
      0 22px 30px rgba(0,0,0,.45);
  }
  .brand {
    display: flex;
    align-items: center;
    gap: 16px;
  }
  .brand-mark {
    width: 58px; height: 58px;
    border: 5px solid currentColor;
    border-radius: 50%;
    flex: none;
  }
  .brand-name {
    font-weight: 800;
    font-size: 40px;
    letter-spacing: .5px;
    line-height: 1;
    white-space: nowrap;
  }

  .card-front {
    background: linear-gradient(135deg, var(--orange-light) 0%, var(--orange) 50%, var(--orange-deep) 100%);
    display: flex;
    align-items: center;
    justify-content: center;
    color: var(--white);
  }

  .card-back {
    background: linear-gradient(160deg, var(--charcoal-top) 0%, var(--charcoal-bottom) 100%);
    padding: 44px 60px;
    color: var(--orange);
  }
  .card-back .brand-mark { width: 46px; height: 46px; border-width: 4px; }
  .card-back .brand-name { font-size: 32px; }

  .person { margin: 26px 0 0 62px; }
  .person-name {
    color: var(--orange);
    font-weight: 800;
    font-size: 22px;
    text-transform: uppercase;
    letter-spacing: .5px;
    line-height: 1.2;
  }
  .person-role {
    color: var(--soft);
    font-weight: 500;
    font-size: 17px;
    margin-top: 4px;
  }
  .contact-list { list-style: none; margin: 20px 0 0 62px; }
  .contact-list li {
    display: flex;
    align-items: center;
    gap: 12px;
    color: var(--white);
    font-size: 16px;
    line-height: 1;
    margin-bottom: 12px;
  }
  .contact-list svg { width: 20px; height: 20px; flex: none; }
  .social-dot {
    width: 20px; height: 20px;
    border-radius: 50%;
    background: var(--orange);
    flex: none;
  }
</style>
</head>
<body>
  <section class="card card-front">
    <div class="brand">
      <span class="brand-mark"></span>
      <span class="brand-name">DRIFTFRAME studio</span>
    </div>
  </section>

  <section class="card card-back">
    <div class="brand">
      <span class="brand-mark"></span>
      <span class="brand-name">DRIFTFRAME studio</span>
    </div>
    <div class="person">
      <p class="person-name">Marcus Ellery</p>
      <p class="person-role">Filmmaker/Photographer</p>
    </div>
    <ul class="contact-list">
      <li>
        <svg viewBox="0 0 24 24" aria-hidden="true"><path fill="#f47a1f" d="M6.6 10.8a15 15 0 0 0 6.6 6.6l2.2-2.2a1 1 0 0 1 1-.25 11.4 11.4 0 0 0 3.6.57 1 1 0 0 1 1 1V20a1 1 0 0 1-1 1A17 17 0 0 1 3 4a1 1 0 0 1 1-1h3.5a1 1 0 0 1 1 1c0 1.25.2 2.45.57 3.57a1 1 0 0 1-.25 1z"/></svg>
        +971528306457
      </li>
      <li>
        <svg viewBox="0 0 24 24" aria-hidden="true"><rect x="2" y="5" width="20" height="14" rx="1.5" fill="#f47a1f"/><path d="M3 6l9 7 9-7" fill="none" stroke="#2b2b30" stroke-width="1.8"/></svg>
        marcus@driftframestudio.example
      </li>
      <li>
        <svg viewBox="0 0 24 24" aria-hidden="true"><g fill="none" stroke="#f47a1f" stroke-width="1.8"><circle cx="12" cy="12" r="9.5"/><ellipse cx="12" cy="12" rx="4.2" ry="9.5"/><path d="M2.5 12h19M4 7h16M4 17h16"/></g></svg>
        www.driftframestudio.example
      </li>
      <li>
        <svg viewBox="0 0 24 24" aria-hidden="true"><path fill="#f47a1f" d="M12 2a7 7 0 0 0-7 7c0 5.2 7 13 7 13s7-7.8 7-13a7 7 0 0 0-7-7zm0 9.5A2.5 2.5 0 1 1 12 6.5a2.5 2.5 0 0 1 0 5z"/></svg>
        PoBox 584193, Dubai, UAE
      </li>
      <li>
        <span class="social-dot"></span>
        @driftframestudio
      </li>
    </ul>
  </section>
</body>
</html>
```